Hydrographic business needs a business card that reaches hunters and off-road enthusiasts

We need a business card for a new hydrographics company catering to customers such as hunters, off-road ATV riders and custom vehicle enthusiasts. A western theme is preferred but professional. Our service should be thought of as upper end graphic design on firearms, off road vehicles, motorcycles, etc... See www.caldorfx.com for ideas on patterns, colors, etc...

Target Market(s)

Hunters, off road enthusiasts, custom car enthusiasts, motorcycle riders...

Industry/Entity Type

Graphic Design

```html
<!DOCTYPE html>
<html lang="en">
<head>
<meta charset="UTF-8">
<title>Caldor Hydro Graphics – Business Card</title>
<link rel="stylesheet" href="https://fonts.googleapis.com/css2?family=Cormorant+Garamond:ital,wght@1,500;1,600&family=Montserrat:wght@400;800&display=swap">
<style>
  :root {
    --backdrop: #2a2a2c;
    --card: #ffffff;
    --card-soft: #f1f1f1;
    --brand-red: #8e1b1f;
    --brand-red-dark: #5e1013;
    --ink: #3c3c3c;
    --photo-sky: #9cb8d8;
    --photo-sand: #e2cfae;
    --photo-dark: #1d2233;
  }
  * { box-sizing: border-box; margin: 0; padding: 0; }
  html, body { width: 1200px; height: 800px; overflow: hidden; }
  body {
    background: var(--backdrop);
    display: flex;
    align-items: center;
    justify-content: center;
    gap: 40px;
    font-family: "Montserrat", Arial, sans-serif;
  }
  .card {
    position: relative;
    width: 550px;
    height: 314px;
    background: var(--card);
    overflow: hidden;
    box-shadow: 0 10px 30px rgba(0,0,0,.45);
  }
  .photo {
    position: absolute;
    background: linear-gradient(180deg, var(--photo-sky) 0%, var(--photo-sky) 28%, var(--photo-dark) 30%, var(--photo-dark) 62%, var(--photo-sand) 64%, var(--photo-sand) 100%);
  }
  .brand-name {
    font-family: "Cormorant Garamond", Georgia, serif;
    font-style: italic;
    font-weight: 600;
    color: var(--brand-red);
    white-space: nowrap;
    line-height: 1;
  }

  /* Front card */
  .card-front .photo { left: 18px; top: 46px; width: 360px; height: 218px; }
  .card-front .brand-name {
    position: absolute;
    top: 14px;
    right: 14px;
    font-size: 25px;
    transform: rotate(180deg);
  }
  .tagline {
    position: absolute;
    left: 0; right: 0;
    bottom: 20px;
    text-align: center;
    font-size: 11px;
    font-weight: 800;
    letter-spacing: .3px;
    color: var(--brand-red);
  }

  /* Back card */
  .card-back { background: var(--card-soft); }
  .card-back .band { position: absolute; inset: 0; }
  .card-back .brand-name {
    position: absolute;
    left: 140px;
    top: 134px;
    font-size: 31px;
    transform: rotate(-14deg);
    transform-origin: left center;
    z-index: 1;
  }
  .card-back .photo { left: 0; top: 172px; width: 232px; height: 110px; }
  .contact-list {
    position: absolute;
    left: 360px;
    top: 118px;
    list-style: none;
    font-size: 11px;
    color: var(--brand-red);
  }
  .contact-list li { display: flex; align-items: center; gap: 10px; height: 24px; }
  .contact-list svg { width: 11px; height: 11px; fill: var(--ink); }
  .address {
    position: absolute;
    left: 30px;
    bottom: 18px;
    font-size: 13px;
    font-weight: 800;
    color: var(--brand-red);
  }
  .pin { position: absolute; right: 26px; bottom: 36px; width: 14px; height: 20px; }
</style>
</head>
<body>

  <section class="card card-front">
    <div class="photo" role="img" aria-label="Photo of a dark custom off-road buggy jumping over a sand dune"></div>
    <div class="brand-name">Caldor Hydro Graphics</div>
    <p class="tagline">THE BEST AND MOST RELIABLE HYDROGRAPHICS SERVICE IN EAST TEXAS</p>
  </section>

  <section class="card card-back">
    <svg class="band" viewBox="0 0 550 314" preserveAspectRatio="none" aria-hidden="true">
      <path d="M0 0 H550 V10 C350 40 150 90 0 150 Z" fill="var(--brand-red)"/>
      <path d="M550 10 C350 40 150 90 0 150" fill="none" stroke="var(--brand-red-dark)" stroke-width="3"/>
      <path d="M550 17 C350 47 150 97 0 157" fill="none" stroke="#ffffff" stroke-width="4"/>
    </svg>
    <div class="brand-name">Caldor Hydro Graphics</div>
    <div class="photo" role="img" aria-label="Photo of a dark custom off-road buggy jumping over a sand dune"></div>
    <ul class="contact-list">
      <li>
        <svg viewBox="0 0 24 24"><path d="M6.6 10.8a15.1 15.1 0 0 0 6.6 6.6l2.2-2.2a1 1 0 0 1 1-.25 11.4 11.4 0 0 0 3.6.57 1 1 0 0 1 1 1V20a1 1 0 0 1-1 1A17 17 0 0 1 3 4a1 1 0 0 1 1-1h3.5a1 1 0 0 1 1 1c0 1.250.2 2.45.57 3.57a1 1 0 0 1-.25 1z"/></svg>
        <span>972 555 0148</span>
      </li>
      <li>
        <svg viewBox="0 0 24 24"><path d="M12 2a10 10 0 1 0 0 20 10 10 0 0 0 0-20zm6.9 6h-3a15.7 15.7 0 0 0-1.3-3.6A8 8 0 0 1 18.9 8zM12 4a14 14 0 0 1 1.9 4h-3.8A14 14 0 0 1 12 4zM4.3 14a8 8 0 0 1 0-4h3.4a16 16 0 0 0 0 4zm.8 2h3a15.7 15.7 0 0 0 1.3 3.6A8 8 0 0 1 5.1 16zm3-8h-3a8 8 0 0 1 4.3-3.6A15.7 15.7 0 0 0 8.1 8zM12 20a14 14 0 0 1-1.9-4h3.8A14 14 0 0 1 12 20zm2.3-6H9.7a14.5 14.5 0 0 1 0-4h4.6a14.5 14.5 0 0 1 0 4zm.3 5.6a15.7 15.7 0 0 0 1.3-3.6h3a8 8 0 0 1-4.3 3.6zm1.7-5.6a16 16 0 0 0 0-4h3.4a8 8 0 0 1 0 4z"/></svg>
        <span>www.caldorfx.com</span>
      </li>
      <li>
        <svg viewBox="0 0 24 24"><path d="M2 5h20v14H2zm2 2v.5l8 5 8-5V7zm0 2.9V17h16V9.9l-8 5z"/></svg>
        <span>studio@caldorfx.com</span>
      </li>
    </ul>
    <svg class="pin" viewBox="0 0 14 20" aria-hidden="true">
      <path d="M7 0a7 7 0 0 0-7 7c0 5 7 13 7 13s7-8 7-13a7 7 0 0 0-7-7zm0 10a3 3 0 1 1 0-6 3 3 0 0 1 0 6z" fill="var(--ink)"/>
    </svg>
    <p class="address">212 Mesa County Road 1450, Pine Ridge, TX, United States</p>
  </section>

</body>
</html>
```